Night Dresses business cards business requirers

We are a new company initiating Mexico operations. Our core business is Night woman dress (both formal and party dress) for rent. Gownhaven is the name of the company. ITS Gownhaven form by two word. The dress word and topia (Utopic) so the place Gownhaven Means That You cant get the ideal, perfect and unique dress for your event. So we would like a modern, very creative, and attractive business card.

Industry/Entity Type

Womens Clothing

Contact Information for Business Card

Rounded Borders, two faces

Requirements
Must have
• Rounded borders, logo and slogan, modern, glam, attractive design
Should not have
• modern design classic or not

```html
<!DOCTYPE html>
<html lang="en">
<head>
<meta charset="utf-8">
<title>Gownhaven Business Card</title>
<link href="https://fonts.googleapis.com/css2?family=Josefin+Sans:wght@400&family=Cormorant+Garamond:wght@500&display=swap" rel="stylesheet">
<style>
  :root {
    --page-bg: #e7e8e9;
    --card-white: #ffffff;
    --band-dark: #31313d;
    --accent-blue: #2aa4dc;
    --disc-light: #d9dbd9;
    --disc-mid: #b1b2b3;
    --brand-pink: #b95ba6;
    --brand-grey: #505052;
    --ink: #2a2a2a;
    --icon: #ffffff;
  }
  html, body {
    margin: 0;
    padding: 0;
    width: 1200px;
    height: 1200px;
    overflow: hidden;
    background: var(--page-bg);
  }
  .canvas {
    position: relative;
    width: 1200px;
    height: 1200px;
  }
  .card {
    position: absolute;
    left: 142.4px;
    width: 915.2px;
    height: 522.4px;
    display: block;
  }
  .card--front { top: 41.6px; }
  .card--back { top: 642.4px; }
  .card-base { fill: var(--card-white); }
  .band { fill: var(--band-dark); }
  .cutout { fill: var(--card-white); }
  .disc--front { fill: var(--disc-light); }
  .disc--back { fill: var(--disc-mid); }
  .accent-bar { fill: var(--accent-blue); }
  .contact-icon { fill: var(--icon); }
  .contact-icon-line { fill: none; stroke: var(--band-dark); stroke-width: 2; }
  .globe-line { fill: none; stroke: var(--icon); stroke-width: 3.5; }
  .brand-ring { fill: none; stroke: var(--brand-pink); stroke-width: 5; }
  .brand-name {
    font-family: "Josefin Sans", sans-serif;
    font-weight: 400;
    fill: var(--brand-grey);
  }
  .slogan {
    font-family: "Cormorant Garamond", serif;
    font-weight: 500;
    font-size: 36px;
    fill: var(--ink);
  }
</style>
</head>
<body>
<main class="canvas">

  <svg class="card card--front" viewBox="0 0 1144 653" aria-label="Card front">
    <rect class="card-base" x="0" y="0" width="1144" height="653" rx="40"/>
    <rect class="band" x="0" y="81" width="915" height="481"/>
    <circle class="cutout" cx="915" cy="323" r="253"/>
    <circle class="disc--front" cx="914" cy="323" r="197"/>
    <rect class="accent-bar" x="0" y="157" width="14" height="331"/>

    <g class="contact-icons">
      <g class="icon-phone" transform="translate(82 233)">
        <path class="contact-icon" d="M-28 -12 Q-28 -24 0 -24 Q28 -24 28 -12 L28 -6 L16 -6 L16 -12 L-16 -12 L-16 -6 L-28 -6 Z"/>
        <path class="contact-icon" d="M-20 -8 L20 -8 L24 22 L-24 22 Z"/>
        <g fill="var(--band-dark)">
          <circle cx="-7" cy="2" r="2"/><circle cx="0" cy="2" r="2"/><circle cx="7" cy="2" r="2"/>
          <circle cx="-7" cy="8" r="2"/><circle cx="0" cy="8" r="2"/><circle cx="7" cy="8" r="2"/>
          <circle cx="-7" cy="14" r="2"/><circle cx="0" cy="14" r="2"/><circle cx="7" cy="14" r="2"/>
        </g>
      </g>
      <g class="icon-mail" transform="translate(82 325)">
        <rect class="contact-icon" x="-28" y="-18" width="56" height="36" rx="2"/>
        <path class="contact-icon-line" d="M-26 -16 L0 6 L26 -16 M-26 16 L-8 0 M26 16 L8 0"/>
      </g>
      <g class="icon-web" transform="translate(82 423)">
        <circle class="globe-line" r="24"/>
        <ellipse class="globe-line" rx="11" ry="24"/>
        <line class="globe-line" x1="0" y1="-24" x2="0" y2="24"/>
        <line class="globe-line" x1="-24" y1="0" x2="24" y2="0"/>
        <line class="globe-line" x1="-20" y1="-12" x2="20" y2="-12"/>
        <line class="globe-line" x1="-20" y1="12" x2="20" y2="12"/>
      </g>
    </g>

    <g class="brand-lockup">
      <circle class="brand-ring" cx="914" cy="267" r="68"/>
      <text class="brand-name" x="914" y="388" font-size="40" letter-spacing="7" text-anchor="middle">GOWNHAVEN</text>
    </g>
  </svg>

  <svg class="card card--back" viewBox="0 0 1144 653" aria-label="Card back">
    <rect class="card-base" x="0" y="0" width="1144" height="653" rx="40"/>
    <rect class="band" x="0" y="82" width="1144" height="480"/>
    <circle class="cutout" cx="573" cy="323" r="253"/>
    <circle class="disc--back" cx="573" cy="323" r="197"/>
    <rect class="accent-bar" x="0" y="158" width="14" height="330"/>

    <g class="brand-lockup">
      <circle class="brand-ring" cx="437" cy="323" r="42"/>
      <text class="brand-name" x="497" y="335" font-size="32" letter-spacing="5">GOWNHAVEN</text>
    </g>

    <text class="slogan" x="582" y="621" text-anchor="middle">Perfect and unique dress for your event</text>
  </svg>

</main>
</body>
</html>
```